Asphalt Driveway Billboard Design

We need a billboard designed for an Asphalt & Concrete Company in Minnesota. We want to advertise Asphalt Driveways on this billboard! Logo is uploaded below. Our website is tamlin-paving.com for more information.

```html
<!DOCTYPE html>
<html lang="en">
<head>
<meta charset="utf-8">
<title>Tamlin Paving – Asphalt Driveway Billboard</title>
<link href="https://fonts.googleapis.com/css2?family=Montserrat:wght@600;700;800;900&display=swap" rel="stylesheet">
<style>
  :root {
    --stage: #3f3b3d;
    --white: #ffffff;
    --ink: #231f20;
    --bar: #262223;
    --blue: #0a62ad;
    --blue-deep: #07508f;
    --sky-blue: #5cc3f2;
    --leaf: #4f7a2c;
    --leaf-light: #86b548;
    --siding: #6b7076;
    --asphalt: #8d8a8f;
  }
  * { box-sizing: border-box; margin: 0; padding: 0; }
  html, body {
    width: 1200px; height: 1200px; overflow: hidden;
    background: var(--stage);
    font-family: "Montserrat", sans-serif;
  }
  .billboard {
    position: absolute; left: 40px; top: 344px;
    width: 1120px; height: 512px;
    background: var(--white);
    overflow: hidden;
  }
  .hero-photo {
    position: absolute; left: 220px; top: 0; width: 900px; height: 440px;
    background:
      linear-gradient(to right, var(--white) 0%, rgba(255,255,255,0.85) 12%, rgba(255,255,255,0.35) 32%, rgba(255,255,255,0) 48%),
      linear-gradient(to bottom, var(--leaf) 0%, var(--leaf-light) 10%, var(--siding) 24%, #7d8287 55%, #a9a7ab 66%, var(--asphalt) 100%);
  }
  .hero-photo::after {
    content: ""; position: absolute; inset: 0;
    background: linear-gradient(to left, rgba(110,160,60,0.9) 0%, rgba(110,160,60,0) 14%);
  }
  .brand {
    position: absolute; left: 40px; top: 150px; width: 400px;
    text-align: center; color: var(--ink); font-weight: 800;
  }
  .brand-dot {
    width: 120px; height: 120px; border-radius: 50%;
    background: var(--blue); margin: 0 auto 22px;
  }
  .brand-name { font-size: 64px; line-height: 1; letter-spacing: 1px; }
  .brand-tag { font-size: 19px; letter-spacing: 2px; margin-top: 10px; }
  .headline {
    position: absolute; left: 480px; top: 300px; width: 620px;
    text-align: center; color: var(--blue);
    font-weight: 900; font-size: 46px; line-height: 1.02; text-transform: uppercase;
    text-shadow: 2px 2px 0 var(--white), -2px -2px 0 var(--white), 2px -2px 0 var(--white), -2px 2px 0 var(--white), 3px 4px 6px rgba(0,0,0,0.45);
  }
  .footer-shapes { position: absolute; left: 0; top: 0; }
  .estimate {
    position: absolute; left: 34px; top: 415px; color: var(--white);
  }
  .estimate-label { color: var(--sky-blue); font-weight: 700; font-size: 24px; letter-spacing: 0.5px; }
  .estimate-phone { font-weight: 800; font-size: 52px; line-height: 1.05; letter-spacing: -1px; }
  .website {
    position: absolute; left: 480px; top: 444px; width: 620px; text-align: center;
    color: var(--white); font-weight: 600; font-size: 39px;
  }
</style>
</head>
<body>
  <main class="billboard">
    <div class="hero-photo" role="img" aria-label="Grey two-storey craftsman house with orange garage doors, trees and a freshly paved asphalt driveway"></div>

    <div class="brand">
      <div class="brand-dot"></div>
      <div class="brand-name">TAMLIN</div>
      <div class="brand-tag">PAVING &amp; CONCRETE</div>
    </div>

    <h1 class="headline">Asphalt Driveway<br>Specialists</h1>

    <svg class="footer-shapes" width="1120" height="512" viewBox="0 0 1120 512">
      <polygon points="0,437 1120,437 1120,512 0,512" fill="var(--bar)"/>
      <polygon points="480,426 1120,426 1120,435 476,435" fill="var(--blue)"/>
      <polygon points="0,405 548,405 470,512 0,512" fill="var(--blue)"/>
      <polygon points="0,495 470,495 462,505 0,505" fill="var(--blue-deep)"/>
    </svg>

    <div class="estimate">
      <div class="estimate-label">REQUEST A FREE ESTIMATE</div>
      <div class="estimate-phone">612-555-0148</div>
    </div>

    <div class="website">www.tamlin-paving.com</div>
  </main>
</body>
</html>
```